Diversity report of banking market in Europe

*Power point presentation style - rather than corporate brochure*
We are an executive recruitment firm who will be sending a report to all our senior clients. We need a designer to make it look eye catching, slick and professional for our audience. The document will be read mainly by PDF so the type of font and size will be very important as will the size of each page.

We have all the content but may need guidance on the amount of text, the size of graphs and inserting some pictures/vectors etc. We can provide more text or cut text back it it helps the design. We can find more graphs if this helps to fill a page

Industry/Entity Type

Investment Banking

Font styles to use
Sans Serif

Colors
0255a3
33b8a4
85cae6
cfeae6
ffffff

Requirements
Must have
• Colours:
11, 29, 49
70, 165, 175
Nice to have
• Have added two example Varnholt documents that we feel are clean and professional. Please use these are our attempt as a guide line to how was want the document to look and feel and flow. Happy to add additional pictures or design to fill out pages. Cant steal actual pictures from varnholt report

```html
<!DOCTYPE html>
<html lang="en">
<head>
<meta charset="utf-8">
<title>Diversity Review in Corporate Credit – Halden Crane</title>
<link href="https://fonts.googleapis.com/css2?family=Montserrat:wght@400;600;700;800&family=Roboto+Condensed:wght@400;700&family=Cinzel:wght@400&display=swap" rel="stylesheet">
<style>
:root{
  --navy:#0b1d31;
  --deep:#12305e;
  --teal:#46a5af;
  --blue:#1f8ee6;
  --bright:#2e7cf6;
  --cyan:#1fd6e0;
  --aqua:#22c3dd;
  --grey:#b9b9c2;
  --ink:#2b2b33;
  --muted:#6b6f78;
  --rule:#7fd3e6;
  --stage:#e4e6ea;
  --paper:#ffffff;
}
*{margin:0;padding:0;box-sizing:border-box}
html,body{width:1200px;height:1200px;overflow:hidden;background:var(--stage)}
body{position:relative;font-family:"Roboto Condensed",sans-serif;color:var(--ink)}
.page{position:absolute;width:496px;height:351px;background:var(--paper);overflow:hidden;box-shadow:0 2px 6px rgba(0,0,0,.12)}
.p1{left:93px;top:52px;background:linear-gradient(90deg,var(--bright),#00e6e0)}
.p2{left:612px;top:52px}
.p3{left:93px;top:424px}
.p4{left:612px;top:424px}
.p5{left:93px;top:797px}
.p6{left:612px;top:797px}
.decor{position:absolute;left:0;top:0;width:496px;height:351px}
.abs{position:absolute}

/* cover */
.cover-address{position:absolute;left:28px;top:266px;border-left:1.2px solid var(--cyan);padding-left:7px;color:#fff;font-family:"Montserrat",sans-serif;font-size:4.3px;line-height:1.35}
.cover-address .phone{margin-top:6px}
.site{position:absolute;font-family:"Cinzel",serif;font-size:6.4px;letter-spacing:.06em}
.cover-site{left:30px;top:321px;color:#fff}

/* title page */
.brand{position:absolute;left:322px;top:33px;font-family:"Montserrat",sans-serif;font-weight:600;font-size:11.5px;letter-spacing:.05em;color:var(--navy);border-bottom:1px solid var(--teal);padding-bottom:2px}
.title-block{position:absolute;left:273px;top:115px;border-left:1.6px solid var(--cyan);padding-left:10px;height:87px}
.report-title{font-family:"Montserrat",sans-serif;font-weight:800;font-size:13px;line-height:1.3;color:var(--navy)}
.report-title .accent{color:var(--teal)}
.report-sub{margin-top:9px;font-family:"Montserrat",sans-serif;font-size:9.6px;line-height:1.4;color:#333}
.byline{position:absolute;left:284px;top:232px;font-family:"Montserrat",sans-serif;font-size:6.6px;color:#333}
.byline b{color:var(--teal);font-weight:600}
.title-site{right:32px;top:321px;color:var(--navy)}

/* section heads */
.section-head{position:absolute;top:44px;border-left:1.6px solid var(--aqua);padding-left:10px}
.section-title{font-family:"Montserrat",sans-serif;font-weight:700;font-size:13.6px;color:var(--blue);letter-spacing:.01em}
.section-title .accent{color:var(--aqua)}
.section-sub{margin-top:7px;font-family:"Montserrat",sans-serif;font-size:10px;color:#222}

.body-text{position:absolute;font-size:3.75px;line-height:1.42;text-align:justify;color:#333}
.body-text p+p{margin-top:4px}
.body-text .hl{color:var(--blue);font-weight:700}
.body-text ul{list-style:none;margin:4px 0 4px 6px}
.body-text li{color:var(--blue);font-weight:700}
.body-text .question{color:var(--blue);font-weight:700;font-style:italic}

.footer{position:absolute;top:332px;font-family:"Cinzel",serif;font-size:5.6px;letter-spacing:.06em;color:#333}
.footer b{font-family:"Montserrat",sans-serif;font-weight:600;color:var(--blue)}
.footer-left{left:52px}
.footer-right{right:32px}

/* chart blocks */
.chart-block{position:absolute;width:147px;height:96px}
.chart-title{border-top:.8px solid var(--rule);border-bottom:.8px solid var(--rule);padding:1.5px 0;text-align:center;font-family:"Montserrat",sans-serif;font-weight:700;font-size:4.2px;color:var(--blue);letter-spacing:.03em;line-height:1.25}
.chart-caption{font-size:3.9px;color:var(--muted);margin-top:3px}
.chart-note{position:absolute;font-size:3.2px;line-height:1.3;color:#444}
.chart-svg{position:absolute}
.legend{font-size:3.2px;color:#444}
.legend span{display:inline-block;width:3px;height:3px;margin-right:2px;vertical-align:middle}
.sw-m{background:var(--blue)}
.sw-f{background:var(--cyan)}
.pie-caption{position:absolute;font-size:3.2px;line-height:1.3;color:#444;width:62px}
.stat-circle{position:absolute;width:58px;height:58px;border-radius:50%;display:flex;flex-direction:column;align-items:center;justify-content:center;color:#fff;text-align:center}
.stat-circle .num{font-family:"Montserrat",sans-serif;font-weight:700;font-size:11.5px;line-height:1}
.stat-circle .lbl{font-family:"Montserrat",sans-serif;font-size:2.8px;line-height:1.3;margin-top:2px;letter-spacing:.03em}
.circle-cyan{background:var(--cyan)}
.circle-blue{background:var(--blue)}
.pyramid-label{position:absolute;font-size:3px;line-height:1.25;text-align:center;color:#222;font-weight:700}
</style>
</head>
<body>

<!-- Cover -->
<section class="page p1">
  <svg class="decor" viewBox="0 0 496 351" aria-hidden="true">
    <polygon points="320,175 496,0 496,351" fill="var(--deep)"/>
    <polygon points="313,64 424,175 313,286 202,175" fill="none" stroke="#fff" stroke-width="1"/>
  </svg>
  <address class="cover-address" style="font-style:normal">
    14 Larkfield Row,<br>Marylebone, London,<br>England W1U 4QX, United Kingdom
    <div class="phone">Office: +44 (0) 20 7946 0182</div>
  </address>
  <div class="site cover-site">WWW.HALDENCRANE.COM</div>
</section>

<!-- Title page -->
<section class="page p2">
  <svg class="decor" viewBox="0 0 496 351" aria-hidden="true">
    <defs>
      <linearGradient id="gTitle" x1="0" x2="1" y1="0" y2="0">
        <stop offset="0" stop-color="#2e7cf6"/><stop offset="1" stop-color="#00e6e0"/>
      </linearGradient>
    </defs>
    <polygon points="0,0 94,94 0,351" fill="var(--deep)"/>
    <polygon points="121,65 231,175 121,285 11,175" fill="#fff" stroke="#c8ecef" stroke-width="1.5"/>
    <polygon points="121,88 208,175 121,262 34,175" fill="url(#gTitle)"/>
    <polygon points="208,223 256,271 208,319 160,271" fill="var(--cyan)"/>
  </svg>
  <div class="brand">HALDEN CRANE</div>
  <div class="title-block">
    <h1 class="report-title"><span class="accent">DIVERSITY</span> REVIEW<br>IN CORPORATE <span class="accent">CREDIT</span></h1>
    <p class="report-sub">Gender &amp; Ethnicity within<br>Credit Investment Management<br>&amp; Leveraged Finance</p>
  </div>
  <p class="byline">Written by <b>Clara Moreau</b></p>
  <div class="site title-site">WWW.HALDENCRANE.COM</div>
</section>

<!-- Introduction -->
<section class="page p3">
  <svg class="decor" viewBox="0 0 496 351" aria-hidden="true">
    <defs>
      <linearGradient id="gIntro" x1="0" x2="1"><stop offset="0" stop-color="#2e7cf6"/><stop offset="1" stop-color="#00e6e0"/></linearGradient>
    </defs>
    <polygon points="496,72 378,190 496,308" fill="var(--grey)"/>
    <polygon points="425,51 495,121 425,191 355,121" fill="#fff" stroke="#c8ecef" stroke-width="1.4"/>
    <polygon points="425,73 473,121 425,169 377,121" fill="url(#gIntro)"/>
  </svg>
  <header class="section-head" style="left:52px">
    <h2 class="section-title">Introduction</h2>
    <p class="section-sub">Halden Crane, A Diversity Review</p>
  </header>
  <div class="body-text" style="left:63px;top:88px;width:140px">
    <p>Gender remains the central diversity question across asset management, yet recent social movements have pushed ethnicity firmly onto the agenda as well. Firms across the financial services industry are now being asked to explain the gaps within their own organisations, and many public reviews have highlighted unbalanced representation at board level. Most of that coverage focuses on the most senior seats. Far less attention is paid to the mid-level and junior pipeline, where the shape of future leadership is decided. As a specialist search firm working across the credit markets, we wanted to look at the numbers ourselves. In this report we analyse the figures, offer our interpretation where the data allows, and leave room for readers to draw their own conclusions. Our aim is simple: to give heads of business and senior HR professionals a clear view of what the market looks like today, broken down by strategy and seniority, alongside the adjacent markets that feed it, and importantly the market that feeds all</p>
  </div>
  <div class="body-text" style="left:210px;top:88px;width:140px">
    <p>of these buyside strategies, the investment banking teams. Beyond this we have analysed the markets that supply talent to the industry as a whole, comparing diversity across investment banking and investment management with other numerate professions.</p>
    <p>Halden Crane is a search firm with an established and credible track record in credit. Our research team has mapped the market line by line, allowing us to show exactly how each figure in this report was calculated. We are also happy to present the underlying data in a spreadsheet format on request.</p>
    <p>Our approach to tracking information places us in a strong position to conduct a gender and ethnicity review of this scale. We reviewed 420 teams within 358 firms across Direct Lending, CLOs, Distressed Debt and Special Situations, together with leveraged finance, restructuring and distressed debt teams in investment banking and advisory firms.</p>
  </div>

  <div class="chart-block" style="left:62px;top:225px">
    <div class="chart-title">GENDER DIVERSITY ACROSS EACH STRATEGY</div>
    <svg class="chart-svg" style="left:0;top:10px" width="100" height="76" viewBox="0 0 100 76" role="img" aria-label="Stacked bar chart of male and female professionals by strategy">
      <g font-family="Roboto Condensed, sans-serif" font-size="3.4" fill="#fff">
        <text transform="translate(6,74) rotate(-90)" fill="#333">Bank &amp; Advisory</text>
        <rect x="8" y="22" width="9" height="52" fill="var(--blue)"/><rect x="8" y="11" width="9" height="11" fill="var(--cyan)"/>
        <text transform="translate(14,36) rotate(-90)">1574</text><text transform="translate(14,19) rotate(-90)">340</text>
        <text transform="translate(26,74) rotate(-90)" fill="#333">Distressed</text>
        <rect x="28" y="37" width="9" height="37" fill="var(--blue)"/><rect x="28" y="34" width="9" height="3" fill="var(--cyan)"/>
        <text transform="translate(34,51) rotate(-90)">1132</text><text transform="translate(34,33) rotate(-90)" fill="#333">91</text>
        <text transform="translate(46,74) rotate(-90)" fill="#333">CLO's</text>
        <rect x="48" y="48" width="9" height="26" fill="var(--blue)"/><rect x="48" y="44" width="9" height="4" fill="var(--cyan)"/>
        <text transform="translate(54,60) rotate(-90)">776</text><text transform="translate(54,43) rotate(-90)" fill="#333">134</text>
        <text transform="translate(66,74) rotate(-90)" fill="#333">Direct Lending</text>
        <rect x="68" y="27" width="9" height="47" fill="var(--blue)"/><rect x="68" y="19" width="9" height="8" fill="var(--cyan)"/>
        <text transform="translate(74,40) rotate(-90)">1427</text><text transform="translate(74,26) rotate(-90)">240</text>
      </g>
      <g font-family="Roboto Condensed, sans-serif" font-size="3" fill="#444">
        <rect x="82" y="60" width="3" height="3" fill="var(--blue)"/><text x="87" y="62.6">Male</text>
        <rect x="82" y="66" width="3" height="3" fill="var(--cyan)"/><text x="87" y="68.6">Female</text>
      </g>
    </svg>
    <p class="chart-note" style="left:101px;top:14px;width:46px">The overall gender diversity levels across each strategy are explored further in this report. The chart gives a clear view of male to female ratios for investment professionals in Direct Lending, Distressed, CLOs and Leveraged Finance. Direct Lending as an asset class has the closest male to female ratio, while banking sits at 17% and lending at 14%.</p>
  </div>

  <svg class="chart-svg" style="left:222px;top:243px" width="60" height="60" viewBox="0 0 60 60" role="img" aria-label="Pie chart: 805 female, 4909 male">
    <circle cx="30" cy="30" r="29" fill="var(--blue)"/>
    <path d="M30 30 L30 1 A29 29 0 0 1 52.5 11.7 Z" fill="var(--cyan)"/>
    <g font-family="Montserrat, sans-serif" fill="#fff" text-anchor="middle">
      <text x="34" y="11" font-size="4.6" font-weight="700">805</text><text x="34" y="14.5" font-size="2.4">14% Female</text>
      <text x="30" y="43" font-size="5" font-weight="700">4909</text><text x="30" y="47" font-size="2.6">86% Male</text>
    </g>
  </svg>
  <p class="pie-caption" style="left:222px;top:304px">There are currently 5714 professionals working across Direct Lending, Distressed, CLOs and Leveraged Finance in Europe. 805 (14%) are female and 4909 (86%) are male.</p>
  <svg class="abs" style="left:216px;top:243px" width="1" height="90" aria-hidden="true"><line x1=".5" y1="0" x2=".5" y2="90" stroke="#ccc" stroke-width=".6" transform="translate(50,0)"/></svg>
  <svg class="chart-svg" style="left:291px;top:243px" width="60" height="60" viewBox="0 0 60 60" role="img" aria-label="Pie chart: 672 ethnic minorities, 5042 white">
    <circle cx="30" cy="30" r="29" fill="var(--cyan)"/>
    <path d="M30 30 L30 1 A29 29 0 0 1 49.5 8.5 Z" fill="var(--blue)"/>
    <g font-family="Montserrat, sans-serif" fill="#fff" text-anchor="middle">
      <text x="36" y="10" font-size="4.6" font-weight="700">672</text><text x="36" y="13.5" font-size="2.4">Ethnic Minorities</text>
      <text x="33" y="42" font-size="5" font-weight="700">5042</text><text x="33" y="46" font-size="2.6">White</text>
    </g>
  </svg>
  <p class="pie-caption" style="left:291px;top:304px">672 investment professionals working across Direct Lending, Distressed, CLOs and Leveraged Finance in Europe are from ethnic minorities, whereas 5042 of the workforce is white.</p>
  <svg class="abs" style="left:285px;top:240px" width="2" height="90" aria-hidden="true"><line x1="1" y1="0" x2="1" y2="90" stroke="#ccc" stroke-width=".6"/></svg>

  <div class="footer footer-left">WWW.HALDENCRANE.COM | <b>02</b></div>
</section>

<!-- Gender diversity across strategies -->
<section class="page p4">
  <svg class="decor" viewBox="0 0 496 351" aria-hidden="true">
    <defs>
      <linearGradient id="gStrat" x1="0" x2="1"><stop offset="0" stop-color="#00e6e0"/><stop offset="1" stop-color="#2e7cf6"/></linearGradient>
    </defs>
    <polygon points="65,51 135,121 65,191 -5,121" fill="#fff" stroke="#c8ecef" stroke-width="1.4"/>
    <polygon points="65,73 113,121 65,169 17,121" fill="url(#gStrat)"/>
  </svg>
  <header class="section-head" style="left:168px">
    <h2 class="section-title">Gender Diversity</h2>
    <p class="section-sub">Across All Strategies</p>
  </header>

  <!-- Direct Lending -->
  <div class="chart-block" style="left:168px;top:96px">
    <div class="chart-title">DIRECT LENDING</div>
    <p class="chart-caption">Gender Diversity by Level</p>
    <svg class="chart-svg" style="left:0;top:22px" width="108" height="70" viewBox="0 0 108 70" role="img" aria-label="Bar chart by level, Direct Lending">
      <g font-family="Roboto Condensed, sans-serif" font-size="3.4" fill="#333">
        <text transform="translate(5,68) rotate(-90)">Analysts 1-4 Yrs</text>
        <rect x="7" y="64.9" width="9" height="3.1" fill="var(--cyan)"/><rect x="18" y="59" width="9" height="9" fill="var(--blue)"/>
        <text transform="translate(13,63.5) rotate(-90)">38</text><text transform="translate(24,58) rotate(-90)">110</text>
        <text transform="translate(37,68) rotate(-90)">Mid-Level 5-10 Yrs</text>
        <rect x="39" y="55.7" width="9" height="12.3" fill="var(--cyan)"/><rect x="50" y="12" width="9" height="56" fill="var(--blue)"/>
        <text transform="translate(45,54.5) rotate(-90)">149</text><text transform="translate(56,11) rotate(-90)">681</text>
        <text transform="translate(69,68) rotate(-90)">MD - Partner</text>
        <rect x="71" y="63.6" width="9" height="4.4" fill="var(--cyan)"/><rect x="82" y="15.7" width="9" height="52.3" fill="var(--blue)"/>
        <text transform="translate(77,62.5) rotate(-90)">53</text><text transform="translate(88,14.5) rotate(-90)">636</text>
      </g>
    </svg>
    <p class="chart-note" style="left:110px;top:12px;width:37px">Where we notice the ratio of female representation lowers in both CLOs and Distressed at the junior level, Direct Lending keeps a female to male analyst ratio near 25%, suggesting it is a preferred buyside route for female leveraged finance professionals.</p>
    <div class="legend abs" style="left:110px;top:76px"><span class="sw-m"></span>Male<br><span class="sw-f"></span>Female</div>
  </div>

  <!-- CLOs -->
  <div class="chart-block" style="left:328px;top:96px">
    <div class="chart-title">CLOS</div>
    <p class="chart-caption">Gender Diversity by Level</p>
    <svg class="chart-svg" style="left:0;top:22px" width="108" height="70" viewBox="0 0 108 70" role="img" aria-label="Bar chart by level, CLOs">
      <g font-family="Roboto Condensed, sans-serif" font-size="3.4" fill="#333">
        <text transform="translate(5,68) rotate(-90)">Analysts 1-4 Yrs</text>
        <rect x="7" y="66.4" width="9" height="1.6" fill="var(--cyan)"/><rect x="18" y="60.7" width="9" height="7.3" fill="var(--blue)"/>
        <text transform="translate(13,65) rotate(-90)">10</text><text transform="translate(24,59.5) rotate(-90)">45</text>
        <text transform="translate(37,68) rotate(-90)">Mid-Level 5-10 Yrs</text>
        <rect x="39" y="54" width="9" height="14" fill="var(--cyan)"/><rect x="50" y="12" width="9" height="56" fill="var(--blue)"/>
        <text transform="translate(45,53) rotate(-90)">87</text><text transform="translate(56,11) rotate(-90)">347</text>
        <text transform="translate(69,68) rotate(-90)">MD - Partner</text>
        <rect x="71" y="62" width="9" height="6" fill="var(--cyan)"/><rect x="82" y="22.2" width="9" height="45.8" fill="var(--blue)"/>
        <text transform="translate(77,61) rotate(-90)">37</text><text transform="translate(88,21) rotate(-90)">284</text>
      </g>
    </svg>
    <p class="chart-note" style="left:110px;top:12px;width:37px">Of the buyside options most commonly available to women in leveraged finance, the CLO market has the strongest representation of females in senior positions at 8.8%. Women in direct lending represent 7.7% of the senior workforce, while only 4.7% remain senior in distressed.</p>
    <div class="legend abs" style="left:110px;top:76px"><span class="sw-m"></span>Male<br><span class="sw-f"></span>Female</div>
  </div>

  <!-- Distressed -->
  <div class="chart-block" style="left:168px;top:196px">
    <div class="chart-title">DISTRESSED, SPECIAL SITUATIONS INCLUDING<br>BANK DISTRESSED TEAM</div>
    <p class="chart-caption">Gender Diversity by Level</p>
    <svg class="chart-svg" style="left:0;top:28px" width="108" height="70" viewBox="0 0 108 70" role="img" aria-label="Bar chart by level, Distressed and Special Situations">
      <g font-family="Roboto Condensed, sans-serif" font-size="3.4" fill="#333">
        <text transform="translate(5,68) rotate(-90)">Analysts 1-4 Yrs</text>
        <rect x="7" y="66.5" width="9" height="1.5" fill="var(--cyan)"/><rect x="18" y="65.6" width="9" height="2.4" fill="var(--blue)"/>
        <text transform="translate(13,65) rotate(-90)">6</text><text transform="translate(24,64) rotate(-90)">24</text>
        <text transform="translate(37,68) rotate(-90)">Mid-Level 5-10 Yrs</text>
        <rect x="39" y="62.4" width="9" height="5.6" fill="var(--cyan)"/><rect x="50" y="14.8" width="9" height="53.2" fill="var(--blue)"/>
        <text transform="translate(45,61) rotate(-90)">57</text><text transform="translate(56,13.5) rotate(-90)">540</text>
        <text transform="translate(69,68) rotate(-90)">MD - Partner</text>
        <rect x="71" y="65.2" width="9" height="2.8" fill="var(--cyan)"/><rect x="82" y="12" width="9" height="56" fill="var(--blue)"/>
        <text transform="translate(77,64) rotate(-90)">28</text><text transform="translate(88,11) rotate(-90)">568</text>
      </g>
    </svg>
    <p class="chart-note" style="left:110px;top:17px;width:37px">Single name distressed funds have the lowest representation of female investment professionals in this group, which includes restructuring teams in advisory. The junior ratio is in line with the market, however mid-level and senior female professionals are more than 50% lower than in CLOs and direct lending teams.</p>
    <div class="legend abs" style="left:110px;top:80px"><span class="sw-m"></span>Male<br><span class="sw-f"></span>Female</div>
  </div>

  <!-- Banks & Advisory -->
  <div class="chart-block" style="left:328px;top:196px">
    <div class="chart-title">BANKS &amp; ADVISORY</div>
    <p class="chart-caption">Gender Diversity by Level</p>
    <div class="legend abs" style="left:2px;top:20px"><span class="sw-m"></span>Male<br><span class="sw-f"></span>Female</div>
    <svg class="chart-svg" style="left:0;top:28px" width="108" height="70" viewBox="0 0 108 70" role="img" aria-label="Bar chart by level, Banks and Advisory">
      <g font-family="Roboto Condensed, sans-serif" font-size="3.4" fill="#333">
        <text transform="translate(5,68) rotate(-90)">Analysts 1-4 Yrs</text>
        <rect x="7" y="63.3" width="9" height="4.7" fill="var(--cyan)"/><rect x="18" y="54.1" width="9" height="13.9" fill="var(--blue)"/>
        <text transform="translate(13,62) rotate(-90)">76</text><text transform="translate(24,53) rotate(-90)">223</text>
        <text transform="translate(37,68) rotate(-90)">Mid-Level 5-10 Yrs</text>
        <rect x="39" y="54.2" width="9" height="13.8" fill="var(--cyan)"/><rect x="50" y="12" width="9" height="56" fill="var(--blue)"/>
        <text transform="translate(45,53) rotate(-90)">222</text><text transform="translate(56,11) rotate(-90)">900</text>
        <text transform="translate(69,68) rotate(-90)">MD - Partner</text>
        <rect x="71" y="65.2" width="9" height="2.8" fill="var(--cyan)"/><rect x="82" y="40.1" width="9" height="27.9" fill="var(--blue)"/>
        <text transform="translate(77,64) rotate(-90)">45</text><text transform="translate(88,39) rotate(-90)">448</text>
      </g>
    </svg>
    <p class="chart-note" style="left:110px;top:12px;width:37px">The leveraged finance and restructuring teams are better represented by female professionals than their peer group on the buyside. Gender diversity moves from 25% at analyst to 19% at mid-level and 9% at senior levels. This fall in numbers could be a result of natural fall off and attrition from lost professionals to the buyside.</p>
  </div>

  <div class="footer footer-right">WWW.HALDENCRANE.COM | <b>03</b></div>
</section>

<!-- Seniority -->
<section class="page p5">
  <svg class="decor" viewBox="0 0 496 351" aria-hidden="true">
    <defs>
      <linearGradient id="gSen" x1="0" x2="1"><stop offset="0" stop-color="#2e7cf6"/><stop offset="1" stop-color="#00e6e0"/></linearGradient>
    </defs>
    <polygon points="496,72 378,190 496,308" fill="var(--grey)"/>
    <polygon points="425,51 495,121 425,191 355,121" fill="#fff" stroke="#c8ecef" stroke-width="1.4"/>
    <polygon points="425,73 473,121 425,169 377,121" fill="url(#gSen)"/>
  </svg>
  <header class="section-head" style="left:52px">
    <h2 class="section-title">Gender Diversity <span class="accent">by Seniority</span></h2>
    <p class="section-sub">Female Seniority Within Asset Management</p>
  </header>
  <div class="body-text" style="left:63px;top:88px;width:140px">
    <p>Men dominate the figures of investment professionals working in the European corporate credit markets that we have analysed in this report. Nowhere is this more prevalent than at senior level within these firms, where females account for just 7.4% of senior positions, only 2.9% of the entire workforce we reviewed.</p>
    <p><span class="hl">There are 163 senior females working across these strategies<br>There are 2036 senior males working across these strategies</span><br>Of all 5714 professionals working across these strategies there are 2,199 senior team members and women only account for 7.4% of these, the biggest gap of all three levels. At mid-level women account for 17.3% of professionals, and at junior level for 24.4%.</p>
    <p>A report produced by Fairholm found that 17% of accountants across the UK at partner level are female. Across chartered accountancy, females account for 45% of the work force. What pressures, resistance, choices or factors account for the drop in female representation at a senior level? I could only speculate, and as a woman, a mum and a professional I think there will be several combined factors that may account for this drop. I'm sure</p>
  </div>
  <div class="body-text" style="left:210px;top:88px;width:140px">
    <p>some may review these statistics and conclude that there is systemic patriarchy and male privilege at play. I've questioned my thinking many times over, should I as a woman who believes in equality point to these numbers and feel they represent male dominance, or are the female individuals joining and leaving the non-investment grade corporate credit markets at higher rates than accountancy for other reasons?</p>
    <p>Are the demands and stresses faced in banking unappealing to women at a certain level, do women reach a point in their career where the working hours are simply too much to handle whilst bringing up a family? Is the demographic of senior female professionals in corporate credit weighted with career women who chose not to raise children? Are the women who are attracted to the finance industry fundamentally different from the females who enter accountancy? Have the women who get onto this career path done so for different reasons?</p>
    <p>So many questions, and I'm afraid very difficult questions to answer. Do all these questions play a part, or are women underrepresented in senior management because they are not given the opportunity to progress? I am as intrigued as anyone to know the answer, so I will provide more information so that you can draw your own conclusions.</p>
  </div>

  <div class="chart-block" style="left:62px;top:232px;width:140px">
    <div class="chart-title">% SPLIT OF ALL MALES TO FEMALES ACROSS<br>ALL STRATEGIES, BY LEVEL</div>
    <svg class="chart-svg" style="left:0;top:14px" width="140" height="68" viewBox="0 0 140 68" role="img" aria-label="Stacked percentage bar chart by level">
      <g font-family="Roboto Condensed, sans-serif" font-size="3.6" fill="#fff">
        <text transform="translate(5,66) rotate(-90)" fill="#333">Senior</text>
        <rect x="7" y="15.4" width="13" height="50.6" fill="var(--blue)"/><rect x="7" y="4" width="13" height="11.4" fill="var(--cyan)"/>
        <text transform="translate(15,46) rotate(-90)">92.6%</text><text transform="translate(15,14) rotate(-90)">7.4%</text>
        <text transform="translate(29,66) rotate(-90)" fill="#333">Mid Level</text>
        <rect x="31" y="19.5" width="13" height="46.5" fill="var(--blue)"/><rect x="31" y="7" width="13" height="12.5" fill="var(--cyan)"/>
        <text transform="translate(39,50) rotate(-90)">82.7%</text><text transform="translate(39,18) rotate(-90)">17.3%</text>
        <text transform="translate(53,66) rotate(-90)" fill="#333">Junior</text>
        <rect x="55" y="30" width="13" height="36" fill="var(--blue)"/><rect x="55" y="12" width="13" height="18" fill="var(--cyan)"/>
        <text transform="translate(63,59) rotate(-90)">75.6%</text><text transform="translate(63,28) rotate(-90)">24.4%</text>
      </g>
      <g font-family="Roboto Condensed, sans-serif" font-size="3" fill="#444">
        <rect x="114" y="52" width="3" height="3" fill="var(--blue)"/><text x="119" y="54.6">Male</text>
        <rect x="114" y="58" width="3" height="3" fill="var(--cyan)"/><text x="119" y="60.6">Female</text>
      </g>
    </svg>
  </div>
  <svg class="abs" style="left:266px;top:232px" width="2" height="80" aria-hidden="true"><line x1="1" y1="0" x2="1" y2="80" stroke="#ccc" stroke-width=".6"/></svg>
  <div class="stat-circle circle-cyan" style="left:211px;top:242px"><span class="num">14%</span><span class="lbl">PERCENTAGE OF<br>FEMALES OVERALL</span></div>
  <div class="stat-circle circle-blue" style="left:292px;top:242px"><span class="num">7.4%</span><span class="lbl">PERCENTAGE OF<br>FEMALE HOLDING<br>A SENIOR POSITION</span></div>

  <svg class="abs" style="left:371px;top:218px" width="52" height="114" viewBox="0 0 52 114" aria-hidden="true">
    <polygon points="12,14 40,14 48,112 4,112" fill="#e3e3e8"/>
  </svg>
  <p class="pyramid-label" style="left:371px;top:211px;width:52px;font-weight:700">Ratio of<br>Female to Male<br>professionals</p>
  <div class="abs" role="img" aria-label="Rows of figure icons showing senior ratio of 1 female to 13.5 males" style="left:382px;top:234px;width:30px;height:18px;background:linear-gradient(180deg,var(--blue),var(--aqua));border-radius:2px"></div>
  <p class="pyramid-label" style="left:371px;top:254px;width:52px">Senior Level:<br>1 to every 13.5</p>
  <div class="abs" role="img" aria-label="Row of figure icons showing mid-level ratio of 1 female to 5 males" style="left:384px;top:268px;width:26px;height:9px;background:linear-gradient(180deg,var(--blue),var(--aqua));border-radius:2px"></div>
  <p class="pyramid-label" style="left:371px;top:279px;width:52px">Mid-Level:<br>1 to every 5</p>
  <div class="abs" role="img" aria-label="Row of figure icons showing junior ratio of 1 female to 3 males" style="left:386px;top:294px;width:22px;height:9px;background:linear-gradient(180deg,var(--blue),var(--aqua));border-radius:2px"></div>
  <p class="pyramid-label" style="left:371px;top:305px;width:52px">Junior Level:<br>1 to every 3</p>

  <div class="footer footer-left">WWW.HALDENCRANE.COM | <b>04</b></div>
</section>

<!-- Gender split across fund managers -->
<section class="page p6">
  <svg class="decor" viewBox="0 0 496 351" aria-hidden="true">
    <defs>
      <linearGradient id="gSplit" x1="0" x2="1"><stop offset="0" stop-color="#00e6e0"/><stop offset="1" stop-color="#2e7cf6"/></linearGradient>
    </defs>
    <polygon points="65,51 135,121 65,191 -5,121" fill="#fff" stroke="#c8ecef" stroke-width="1.4"/>
    <polygon points="65,73 113,121 65,169 17,121" fill="url(#gSplit)"/>
  </svg>
  <header class="section-head" style="left:178px">
    <h2 class="section-title">Gender Diversity <span class="accent">by Seniority</span></h2>
    <p class="section-sub">The Gender Split Across Credit Fund Managers</p>
  </header>
  <div class="body-text" style="left:178px;top:88px;width:140px">
    <p>The adjacent chart further breaks down the gender split of female to male professionals across all levels. The analysis highlights the disparity between male and female numbers, which increases with seniority. The average of every female to male changes from:</p>
    <ul><li>• 1 to every 3 at Analyst level</li><li>• 1 to every 5 at Mid-level</li><li>• 1 to every 13 at a Senior level</li></ul>
    <p>One of the many big questions faced by HR professionals and heads of business concerned with the level of gender diversity in their business is to what degree they manage expectations by these averages. Is it fair to interview a female candidate and hold her to the same level of expectations, knowing that statistically she has a 1 in 4 chance of being the strongest candidate for the role based on gender?</p>
    <p>Let's look at this another way. Let's say that every female analyst in banking is equally as competent as every male, and there is still a ratio of 1 in every 4 candidates you interview being female. In this example you would simply need to interview 8 candidates to be able to choose from 2 strong female candidates, and as you wish to address the gender diversity levels in your team, you decide to choose the female candidate that most fits your company's culture and values. But we know that no two candidates are equally matched in modelling, commercial understanding of key risks and drivers; two candidates may have equal credit training, or have worked on the same number of transactions, yet not speak the same languages or share similar personalities. Each candidate brings a different combination of strengths, and those differences help a hiring manager decide who best meets the requirements of the role. At the heart of the matter you want the best hire: usually the sharpest candidate who interviews well, has a strong CV, sound technical ability, and who is a strong cultural fit to your organisation.</p>
  </div>
  <div class="body-text" style="left:327px;top:88px;width:140px">
    <p class="question">If it were possible to interview these 8 candidates under a blind test where gender had not been revealed, by the law of averages, would we expect the strongest candidate to be male or female?</p>
    <p>Is positive discrimination more acceptable than negative discrimination? Or should the question really be, are women already unfairly positioned because they have to operate at a far higher level than men to compete? This is a contentious point for many, and rightly so for those standout female bankers who paved the way and would feel undermined if they were not held to the same expectations as their male counterparts. There are many women who would feel this way, and the world needs people from all walks of life that can outperform the law of averages. However, the question remains whether the averages should be calculated into the decision-making process. Where the female to male ratio is 1:1, surely gender is a mute point; where it is 1:13 at senior level, the pressure to work on diversity is a positive force that is most welcome, and the benefits are seen in many ways. In this study we further explore the differences in gender diversity witnessed in credit compared with similar careers and university applications.</p>
  </div>

  <div class="chart-block" style="left:335px;top:206px;width:132px">
    <div class="chart-title">DIRECT SPLIT</div>
    <p class="chart-caption" style="text-align:center">Gender split by level for professionals across<br>all strategies</p>
    <svg class="chart-svg" style="left:0;top:20px" width="132" height="72" viewBox="0 0 132 72" role="img" aria-label="Bar chart of gender split by level across all strategies">
      <g font-family="Roboto Condensed, sans-serif" font-size="3" fill="#444">
        <rect x="4" y="4" width="3" height="3" fill="var(--blue)"/><text x="9" y="6.6">Male</text>
        <rect x="4" y="10" width="3" height="3" fill="var(--cyan)"/><text x="9" y="12.6">Female</text>
      </g>
      <g font-family="Roboto Condensed, sans-serif" font-size="3.6" fill="#333">
        <text transform="translate(10,70) rotate(-90)">Analysts 1-4 Yrs</text>
        <rect x="12" y="67.2" width="10" height="2.8" fill="var(--cyan)"/><rect x="24" y="61.3" width="10" height="8.7" fill="var(--blue)"/>
        <text transform="translate(19,66) rotate(-90)">130</text><text transform="translate(31,60) rotate(-90)">402</text>
        <text transform="translate(46,70) rotate(-90)">Mid-Level 5-10 Yrs</text>
        <rect x="48" y="58.9" width="10" height="11.1" fill="var(--cyan)"/><rect x="60" y="17" width="10" height="53" fill="var(--blue)"/>
        <text transform="translate(55,57.5) rotate(-90)">515</text><text transform="translate(67,16) rotate(-90)">2468</text>
        <text transform="translate(82,70) rotate(-90)">MD - Partner</text>
        <rect x="84" y="66.5" width="10" height="3.5" fill="var(--cyan)"/><rect x="96" y="26.3" width="10" height="43.7" fill="var(--blue)"/>
        <text transform="translate(91,65) rotate(-90)">163</text><text transform="translate(103,25) rotate(-90)">2036</text>
      </g>
    </svg>
  </div>

  <div class="footer footer-right">WWW.HALDENCRANE.COM | <b>05</b></div>
</section>

</body>
</html>
```